依頼概要
10月から始める、動物病院の健康診断キャンペーンのDM(ハガキ)のデザインをお願いします

以前、作成したDMを載せておきますので参考にしていただければと思います

必ず入れていただきたい項目(文言はお任せします)
・対象動物:ワンちゃん ネコちゃん ウサギさん
・キャンペーン期間:10月1日から11月30日まで
・キャンペーン内容:
一般健康診断(身体検査、血液検査(血球検査+生化学検査19項目))通常9000が6000円
オプション検査(尿検査、糞便検査、ホルモン検査(甲状腺など)、レントゲン検査、エコー検査)各30%OFF
・エコー検査は電話にて予約が必要
・できれば12時間絶食で来院
・下部に病院の情報

表面(宛名面)
以前と同様に下部に
秋の健康診断キャンペーンの案内
病院の情報(診療時間など)

カミテックさんのポストカード印刷のアートポスト180kg両面印刷でお願いする予定です。
規格はそちらに合わせていただければと思います。

シンプルで分かりやすいものを希望しています。
きっかりしているものよりも、秋らしい雰囲気なもの、可愛らしいものを希望します。

お手数ですが、診療時間などの詳細はHPよりお願いします。
https://www.sorano-vet.example
申し訳ございません
病院のロゴデータを添付し忘れましたので添付しておきます。
よろしくお願いします。
以前のDMデータです
■ 選んだ理由

わかりやすく、かわいらしいデザインで老若男女問わず親しみやすいデザインだったため。

■ 提案者全員のお礼・コメント

このたびは素敵なご提案をたくさんいただきありがとうございます。
どれも甲乙つけがたく、デザインをみさせてもらうのが楽しかったです。
スタッフのアンケートで多数だったものを今回は選ばせていただきました。
また機会がありましたらよろしくお願いいたします。

```html
<!DOCTYPE html>
<html lang="ja">
<head>
<meta charset="utf-8">
<title>秋の健康診断キャンペーン</title>
<link rel="stylesheet" href="https://fonts.googleapis.com/css2?family=M+PLUS+Rounded+1c:wght@400;500;700;800&display=swap">
<style>
  :root {
    --paper: #fcf6e6;
    --orange: #e8782a;
    --orange-deep: #d9621b;
    --brown: #6b4a2f;
    --ink: #3d3128;
    --badge: #f2a23a;
    --highlight: #fbe0b8;
    --leaf-a: #e9a249;
    --leaf-b: #c86a3a;
    --leaf-c: #9fae5a;
    --line: #d9c7a6;
  }
  * { margin: 0; padding: 0; box-sizing: border-box; }
  html, body { width: 811px; height: 1200px; overflow: hidden; background: var(--paper); }
  body { font-family: "M PLUS Rounded 1c", sans-serif; color: var(--ink); }
  .card { position: relative; width: 811px; height: 1200px; background: var(--paper); overflow: hidden; }
  .abs { position: absolute; }

  .targets { top: 26px; left: 0; width: 100%; text-align: center; color: var(--orange); font-weight: 700; font-size: 27px; letter-spacing: 2px; }
  .title { top: 60px; left: 0; width: 100%; text-align: center; color: var(--orange-deep); font-weight: 800; font-size: 68px; letter-spacing: 4px; }
  .subtitle { top: 142px; left: 0; width: 100%; text-align: center; color: var(--orange-deep); font-weight: 800; font-size: 40px; letter-spacing: 3px; }

  .lead { top: 222px; left: 40px; font-size: 23px; line-height: 1.55; font-weight: 500; color: var(--ink); }
  .animals { top: 185px; left: 255px; width: 290px; height: 225px; border-radius: 50% 50% 40% 40%;
    background: radial-gradient(ellipse at 50% 55%, #f4c98a 0%, #e9b06a 45%, rgba(233,176,106,0) 72%); }

  .period-label { top: 190px; left: 588px; width: 190px; height: 42px; border-radius: 21px; background: var(--orange);
    color: #fff; font-size: 20px; font-weight: 700; text-align: center; line-height: 42px; white-space: nowrap; }
  .period { top: 240px; left: 565px; width: 236px; text-align: center; color: var(--orange-deep); font-size: 43px; font-weight: 800; letter-spacing: -1px; white-space: nowrap; }

  .garland { top: 395px; left: 0; width: 811px; height: 80px;
    background: linear-gradient(90deg, rgba(233,162,73,.55), rgba(200,106,58,.45) 30%, rgba(159,174,90,.45) 55%, rgba(233,162,73,.55) 80%, rgba(200,106,58,.4));
    clip-path: polygon(0 40%, 25% 70%, 50% 45%, 75% 75%, 100% 40%, 100% 65%, 75% 100%, 50% 70%, 25% 95%, 0 65%); }

  .section-head { left: 0; width: 100%; text-align: center; color: var(--orange-deep); font-weight: 800; }
  .section-head span { background: linear-gradient(transparent 62%, var(--highlight) 62%); padding: 0 8px; }
  .general-head { top: 490px; font-size: 46px; letter-spacing: 3px; }

  .save-badge { top: 478px; left: 640px; width: 112px; height: 112px; border-radius: 50%; background: var(--badge); color: #fff; text-align: center; }
  .save-badge .amount { display: block; margin-top: 24px; font-size: 18px; font-weight: 700; }
  .save-badge .word { display: block; font-size: 32px; font-weight: 800; line-height: 1.1; }

  .price { top: 560px; left: 0; width: 100%; text-align: center; font-weight: 700; color: var(--ink); }
  .price .regular { font-size: 26px; text-decoration: line-through; text-decoration-color: var(--orange-deep); }
  .price .arrow { font-size: 26px; color: var(--orange-deep); margin: 0 6px; }
  .price .now { font-size: 54px; color: var(--orange-deep); font-weight: 800; }
  .price .yen { font-size: 30px; color: var(--orange-deep); font-weight: 800; }

  .detail { left: 0; width: 100%; text-align: center; font-size: 21px; line-height: 1.65; font-weight: 500; }
  .general-detail { top: 632px; }

  .option-head { top: 710px; font-size: 42px; letter-spacing: 3px; }
  .discount { top: 770px; left: 0; width: 100%; text-align: center; color: var(--orange-deep); font-size: 50px; font-weight: 800; letter-spacing: 2px; }
  .option-detail { top: 852px; }

  .leaves-left { top: 720px; left: 10px; width: 90px; height: 300px; border-radius: 45px;
    background: linear-gradient(180deg, rgba(233,162,73,.5), rgba(200,106,58,.35), rgba(159,174,90,.35)); }
  .leaves-right { top: 690px; left: 716px; width: 85px; height: 330px; border-radius: 42px;
    background: linear-gradient(180deg, rgba(200,106,58,.45), rgba(233,162,73,.45), rgba(159,174,90,.35)); }
  .leaves-bottom { top: 985px; left: 110px; width: 590px; height: 70px; border-radius: 35px;
    background: linear-gradient(90deg, rgba(159,174,90,.35), rgba(233,162,73,.5), rgba(200,106,58,.4), rgba(233,162,73,.45)); }

  .footer-note { top: 1082px; left: 0; width: 100%; text-align: center; font-size: 19px; font-weight: 500; color: var(--ink); }
  .footer-rule { top: 1118px; left: 30px; width: 751px; height: 2px; background: var(--line); }
  .footer { top: 1132px; left: 30px; width: 751px; height: 42px; display: flex; align-items: center; justify-content: space-between; }
  .clinic { display: flex; align-items: center; gap: 10px; color: var(--brown); font-size: 18px; font-weight: 700; white-space: nowrap; }
  .clinic .mark { width: 28px; height: 28px; border-radius: 50%; background: var(--leaf-c); }
  .access { display: flex; align-items: center; gap: 10px; white-space: nowrap; }
  .url { font-size: 19px; font-weight: 700; color: var(--brown); }
  .or { font-size: 15px; font-weight: 500; color: var(--ink); }
  .search { width: 200px; height: 38px; border: 2px solid var(--brown); border-radius: 6px; display: flex; align-items: center; background: #fff; overflow: hidden; }
  .search .query { flex: 1; padding-left: 8px; font-size: 14px; font-weight: 500; color: var(--ink); white-space: nowrap; overflow: hidden; }
  .search .button { width: 36px; height: 100%; background: var(--brown); display: flex; align-items: center; justify-content: center; }
</style>
</head>
<body>
<main class="card">
  <p class="abs targets">ワンちゃん・ネコちゃん・ウサギさん</p>
  <h1 class="abs title">秋の健康診断</h1>
  <p class="abs subtitle">キャンペーン</p>

  <p class="abs lead">寒さが本格化する前に<br>健康チェック<br>してみませんか?</p>
  <div class="abs animals" role="img" aria-label="毛布にくるまる犬・猫・ウサギのイラスト"></div>

  <p class="abs period-label">キャンペーン期間</p>
  <p class="abs period">10/1~11/30</p>

  <div class="abs garland" role="img" aria-label="秋の落ち葉とどんぐりのガーランド飾り"></div>

  <h2 class="abs section-head general-head"><span>一般健康診断</span></h2>
  <div class="abs save-badge"><span class="amount">3,000円</span><span class="word">お得</span></div>
  <p class="abs price"><span class="regular">通常9,000円</span><span class="arrow">→</span><span class="now">6,000</span><span class="yen">円</span></p>
  <p class="abs detail general-detail">身体検査/血液検査(血球検査+生化学検査19項目)<br>できれば12時間絶食でご来院下さい。</p>

  <div class="abs leaves-left" role="img" aria-label="紅葉した葉とどんぐりの飾り"></div>
  <div class="abs leaves-right" role="img" aria-label="紅葉した葉とどんぐりの飾り"></div>

  <h2 class="abs section-head option-head"><span>オプション検査</span></h2>
  <p class="abs discount">各30%OFF</p>
  <p class="abs detail option-detail">尿検査/糞便検査/ホルモン検査(甲状腺など)<br>レントゲン検査/エコー検査(要予約)</p>

  <div class="abs leaves-bottom" role="img" aria-label="落ち葉ときのこの飾り"></div>

  <p class="abs footer-note">その他、詳しくはHPをご覧ください。</p>
  <div class="abs footer-rule"></div>
  <footer class="abs footer">
    <div class="clinic"><span class="mark"></span><span>空野ペットクリニック</span></div>
    <div class="access">
      <span class="url">sorano-vet.example</span>
      <span class="or">又は</span>
      <div class="search">
        <span class="query">空野 ペットクリニック</span>
        <span class="button">
          <svg width="18" height="18" viewBox="0 0 20 20" aria-hidden="true"><circle cx="8" cy="8" r="5.5" fill="none" stroke="#fff" stroke-width="2.4"/><line x1="12" y1="12" x2="17.5" y2="17.5" stroke="#fff" stroke-width="2.6" stroke-linecap="round"/></svg>
        </span>
      </div>
    </div>
  </footer>
</main>
</body>
</html>
```